Direct Mail flyer for the timeshare industry.

We need someone who has experience in direct mail experience in postcards and successful campaigns. The post card we are using is not good at all.

We are looking at a 5.5 x 8.5 postcard with 4 color on one side and the black and white on the mailing side. But if someone has a better idea instead of a postcard then I am open to that

Target Market(s)

Timeshare owners...most of them are 55 plus in age. We help people get out of their time share

Industry/Entity Type

Industry

Font styles to use
Serif

Colors

Designer to choose colors to be used in the design.

Requirements
Must have
• Call to action and be easy to understand and look very professional and not fake or cheesy

```html
<!DOCTYPE html>
<html lang="en">
<head>
<meta charset="utf-8">
<title>Private Event Invitation Postcard</title>
<link rel="stylesheet" href="https://fonts.googleapis.com/css2?family=Lato:wght@400;700;900&display=swap">
<style>
  :root {
    --blue: #3d8bc4;
    --blue-text: #3a8fd0;
    --ink: #3a3a3a;
    --muted: #555a60;
    --band-gray: #6b6d70;
    --coral: #f26452;
    --line: #d4d6d9;
    --paper: #ffffff;
    --backdrop: #e9e6e1;
    --photo-warm: #c99a5c;
    --photo-light: #efe1c4;
  }
  * { box-sizing: border-box; margin: 0; padding: 0; }
  html, body { width: 1200px; height: 1200px; overflow: hidden; }
  body {
    background: var(--backdrop);
    font-family: "Lato", sans-serif;
    color: var(--ink);
    position: relative;
  }
  .postcard {
    position: absolute;
    left: 183px;
    width: 834px;
    height: 540px;
    background: var(--paper);
    box-shadow: 0 6px 18px rgba(0,0,0,.18);
    overflow: hidden;
  }
  .postcard--front { top: 40px; }
  .postcard--back { top: 620px; }

  /* Front: left column */
  .info {
    position: absolute; left: 0; top: 0; width: 390px; height: 495px;
  }
  .headline {
    padding: 22px 12px 0 22px;
    line-height: 1.1;
  }
  .headline__main {
    color: var(--blue-text); font-weight: 900; font-size: 19px; letter-spacing: .2px;
    white-space: nowrap;
  }
  .headline__sub {
    font-size: 19px; font-weight: 400; color: var(--ink); padding-left: 70px;
    white-space: nowrap;
  }
  .venue {
    margin: 8px 22px 0 52px;
    border: 1px solid var(--line);
    border-radius: 8px;
    padding: 7px 14px 8px;
    line-height: 1.12;
  }
  .venue__name { color: var(--blue-text); font-weight: 900; font-size: 18px; }
  .venue__address { color: var(--muted); font-size: 14px; }
  .venue__date { color: var(--blue-text); font-weight: 900; font-size: 17px; margin-top: 4px; }
  .venue__times { font-weight: 700; font-size: 15px; color: var(--ink); }
  .offer {
    margin-top: 10px;
    background: var(--band-gray);
    padding: 7px 18px 9px 24px;
    text-align: center;
    line-height: 1.2;
  }
  .offer__title { color: var(--coral); font-size: 20px; font-weight: 900; }
  .offer__text { color: #fff; font-size: 14px; font-weight: 700; }
  .offer__free { color: var(--coral); }
  .benefits { padding: 9px 18px 0 26px; }
  .benefit {
    border: 1px solid var(--line);
    border-radius: 6px;
    padding: 4px 10px 5px;
    margin-bottom: 6px;
    line-height: 1.18;
  }
  .benefit__label { color: var(--blue-text); font-weight: 900; font-size: 11px; letter-spacing: .4px; }
  .benefit__text { color: var(--muted); font-size: 10px; }
  .rsvp {
    position: absolute; left: 0; bottom: 0; width: 390px; height: 45px;
    background: var(--blue);
    color: #fff; font-weight: 900; font-size: 15px;
    display: flex; align-items: center; justify-content: center;
  }

  /* Front: right column */
  .photo {
    position: absolute; left: 390px; top: 0; width: 444px; height: 450px;
    background:
      linear-gradient(180deg, var(--photo-light) 0%, #e2c592 35%, var(--photo-warm) 70%, #8a5a2e 100%);
  }
  .cta {
    position: absolute; left: 390px; top: 450px; width: 444px; height: 90px;
    background: var(--blue);
    display: flex; flex-direction: column; align-items: center; justify-content: center;
    gap: 6px;
  }
  .cta__pill {
    background: #fff; color: var(--blue-text);
    font-weight: 900; font-size: 17px;
    padding: 5px 16px; border-radius: 4px;
  }
  .cta__text { color: #fff; font-weight: 900; font-size: 16px; letter-spacing: .3px; }

  /* Back */
  .return-address {
    position: absolute; left: 60px; top: 60px;
    font-size: 15px; line-height: 1.2; color: var(--ink); font-style: normal;
  }
  .permit {
    position: absolute; right: 40px; top: 40px;
    width: 128px; border: 1px solid var(--line);
    padding: 8px 6px; text-align: center;
    font-size: 11px; font-weight: 700; line-height: 1.2; color: var(--ink);
  }
  .address-lines {
    position: absolute; left: 490px; top: 300px;
  }
</style>
</head>
<body>

<section class="postcard postcard--front">
  <div class="info">
    <header class="headline">
      <div class="headline__main">A PRIVATE EVENT INVITATION</div>
      <div class="headline__sub">- LIMITED SEATING</div>
    </header>
    <div class="venue">
      <div class="venue__name">Maple Court Suites</div>
      <div class="venue__address">2150 Commerce Parkway<br>Fort Worth, TX 76140</div>
      <div class="venue__date">Saturday, February 17, 2018</div>
      <div class="venue__times">10:30 AM &nbsp;|&nbsp; 3:00 PM &nbsp;|&nbsp; 6:00 PM</div>
    </div>
    <div class="offer">
      <div class="offer__title">THIS IS YOUR CHANCE!</div>
      <div class="offer__text">We've arranged for you and one guest to attend our Ridgeline Owner Group Event <span class="offer__free">FREE</span> of charge.</div>
    </div>
    <div class="benefits">
      <div class="benefit">
        <div class="benefit__label">EDUCATION</div>
        <div class="benefit__text">We promise this event will be an eye-opening experience and an incredible learning opportunity regardless of your current situation.</div>
      </div>
      <div class="benefit">
        <div class="benefit__label">PROTECTION</div>
        <div class="benefit__text">Arm yourself with the knowledge of how to avoid the current scams occurring in the timeshare industry to protect you as an owner.</div>
      </div>
      <div class="benefit">
        <div class="benefit__label">ADVISEMENT</div>
        <div class="benefit__text">Your questions are welcomed and will be addressed. This will bring you the sense of confidence that you have been seeking.</div>
      </div>
    </div>
  </div>
  <div class="rsvp">RSVP Code # ROG70218</div>
  <div class="photo" role="img" aria-label="Photo of a seated audience in a lecture hall facing a presentation screen and speaker panel"></div>
  <div class="cta">
    <div class="cta__pill">CALL (888) 555-0142 TODAY WITH</div>
    <div class="cta__text">TO GUARANTEE YOUR SEATS!</div>
  </div>
</section>

<section class="postcard postcard--back">
  <address class="return-address">
    Ridgeline Owner Group, LLC<br>
    2215 W Ridgeview Lane<br>
    Branson, Mo. 65616
  </address>
  <div class="permit">PRSRT STD<br>US POSTAGE<br>PAID<br>BRANSON MO<br>PERMIT # 2841</div>
  <svg class="address-lines" width="300" height="130" viewBox="0 0 300 130" aria-hidden="true">
    <g stroke="#c4c6c9" stroke-width="2">
      <line x1="0" y1="10" x2="290" y2="10"/>
      <line x1="0" y1="55" x2="290" y2="55"/>
      <line x1="0" y1="100" x2="290" y2="100"/>
    </g>
  </svg>
</section>

</body>
</html>
```